Stylish new business card needed!

Hello everyone! I am in need of a new business card design for an alarm company here in Hurricane WV. I have all fonts, color codes and logos provided for you use! We are a young company and like the style of a clean sleek looking business card. Would like it double sided, one side holding the logo and the other with your design!
Target Market(s)
The people that are looking for the newest tech for home automation and security
Industry/Entity Type
Alarm services; Home automation
Contact Information for Business Card
Name of person; position (Sales; Installer); Phone Number (555.419.7362); Employee cell Number; Website (www.GuardedByVelm.example); Employee Email; Double sided
Look and feel
Each slider illustrates characteristics of the customer's brand and the style your logo design should communicate.

```html
<!DOCTYPE html>
<html lang="en">
<head>
<meta charset="UTF-8">
<title>Guarded by Velm – Business Card</title>
<link href="https://fonts.googleapis.com/css2?family=Montserrat:wght@700&family=Open+Sans:wght@400;600&display=swap" rel="stylesheet">
<style>
  :root {
    --bg: #1c1c1c;
    --orange: #f7924f;
    --orange-deep: #f08a45;
    --grey: #8e8e8e;
    --text: #4a4a4a;
    --white: #ffffff;
  }
  * { margin: 0; padding: 0; box-sizing: border-box; }
  html, body { width: 1200px; height: 801px; overflow: hidden; }
  body {
    background: var(--bg);
    display: flex;
    align-items: center;
    justify-content: center;
    gap: 40px;
    font-family: "Open Sans", sans-serif;
  }
  .card {
    width: 520px;
    height: 297px;
    border-radius: 18px;
    position: relative;
    overflow: hidden;
  }
  .card--front { background: var(--white); display: flex; align-items: center; }
  .card--back {
    background: linear-gradient(110deg, var(--orange-deep) 0%, var(--orange) 55%, var(--orange-deep) 100%);
    display: flex; align-items: center; justify-content: center;
  }
  .brand { display: flex; flex-direction: column; }
  .brand__name {
    font-family: "Montserrat", sans-serif;
    font-weight: 700;
    text-transform: uppercase;
    line-height: 1.05;
    letter-spacing: 1px;
  }
  .brand__tagline {
    font-family: "Montserrat", sans-serif;
    font-weight: 700;
    text-transform: uppercase;
    letter-spacing: 1px;
  }
  .card--front .brand { padding-left: 44px; width: 270px; }
  .card--front .brand__name { color: var(--orange); font-size: 30px; }
  .card--front .brand__tagline { color: var(--orange); font-size: 7.5px; margin-top: 10px; }
  .card--back .brand__name { color: var(--white); font-size: 44px; }
  .card--back .brand__tagline { color: var(--white); font-size: 10.5px; margin-top: 14px; }
  .divider {
    width: 1px; height: 110px;
    background: var(--orange);
    margin: 0 26px 0 6px;
  }
  .contact__name { color: var(--orange); font-weight: 600; font-size: 22px; line-height: 1.1; }
  .contact__role { color: var(--text); font-size: 11px; margin-bottom: 8px; }
  .contact__list { list-style: none; }
  .contact__item {
    display: flex; align-items: center; gap: 7px;
    color: var(--text); font-size: 11.5px; line-height: 1.65;
  }
  .contact__icon { width: 10px; height: 10px; fill: var(--orange); flex: none; }
</style>
</head>
<body>
  <section class="card card--front">
    <div class="brand">
      <span class="brand__name">Guarded by<br>Velm</span>
      <span class="brand__tagline">Automation and security services</span>
    </div>
    <div class="divider"></div>
    <div class="contact">
      <p class="contact__name">Dana Ortiz</p>
      <p class="contact__role">Manager</p>
      <ul class="contact__list">
        <li class="contact__item">
          <svg class="contact__icon" viewBox="0 0 10 10"><rect x="2" y="0" width="6" height="10" rx="1"/><rect x="3" y="1.2" width="4" height="6.5" fill="#fff"/></svg>
          000-000-0000
        </li>
        <li class="contact__item">
          <svg class="contact__icon" viewBox="0 0 10 10"><path d="M2 0.5 L4 2.8 L3 4 Q4.2 6 6 7 L7.2 6 L9.5 8 L8 9.8 Q2.5 8.5 0.3 2 Z"/></svg>
          555.419.7362
        </li>
        <li class="contact__item">
          <svg class="contact__icon" viewBox="0 0 10 10"><rect x="0" y="2" width="10" height="6.5"/><path d="M0 2 L5 5.8 L10 2" stroke="#fff" stroke-width="0.9" fill="none"/></svg>
          mail@GuardedByVelm.example
        </li>
        <li class="contact__item">
          <svg class="contact__icon" viewBox="0 0 10 10"><circle cx="5" cy="5" r="5"/><path d="M0 5 H10 M5 0 Q2 5 5 10 Q8 5 5 0" stroke="#fff" stroke-width="0.7" fill="none"/></svg>
          www.GuardedByVelm.example
        </li>
      </ul>
    </div>
  </section>

  <section class="card card--back">
    <div class="brand">
      <span class="brand__name">Guarded by<br>Velm</span>
      <span class="brand__tagline">Automation and security services</span>
    </div>
  </section>
</body>
</html>
```